Home Refinance . Residential Mortgages

I want to post a small flyer as part of an email. I want do an email blast. I am a mortgage company and want to entice borrowers with my low interest rates. My website is www.oakmerecapital-demo.com
The colors must match the website colors.
VA IRRL REFINANCE.
30 YR. FIXED RATES as low as
2.25% | 2.437% APR
No Appraisal, No out of Pocket cost, NO Income Verification, NO Asset Verification, Close in 30 days or less

Target Market(s)

Real Estate agents & Borrowers looking to get a mortgage loan

Colors
0455a3
ec1f27
28a1d5

Requirements
Must have
• The colors must match the website colors.
OAKMERE CAPITAL, INC,.
4817B Wellsbury Road
Alexandria, VA 22987
QRLA 5830724
www.qrlaborrowerlookup-demo.com

Bright Harbor Pledge LOGO.

```html
<!DOCTYPE html>
<html lang="en">
<head>
<meta charset="utf-8">
<title>Oakmere Capital – VA IRRL Refinance Flyer</title>
<link rel="stylesheet" href="https://fonts.googleapis.com/css2?family=Bebas+Neue&family=Caveat:wght@500&family=Open+Sans:wght@700;800&display=swap">
<style>
  :root {
    --brand-blue: #0455a3;
    --brand-red: #ec1f27;
    --brand-cyan: #28a1d5;
    --footer-blue: #0b52a6;
    --headline-blue: #1d4f9f;
    --paper: #ffffff;
    --tear-shadow: #d9dde0;
  }
  html, body {
    margin: 0;
    padding: 0;
    width: 848px;
    height: 1200px;
    overflow: hidden;
    background: #ffffff;
  }
  .flyer {
    position: relative;
    width: 848px;
    height: 1200px;
    background: var(--paper);
    overflow: hidden;
  }
  .flyer__art {
    position: absolute;
    left: 10px;
    top: 11px;
    width: 828px;
    height: 1178px;
  }
  .brand-tab {
    position: absolute;
    left: 10px;
    top: 46px;
    width: 380px;
    height: 94px;
    background: var(--paper);
    clip-path: polygon(0 0, 88% 0, 100% 100%, 0 100%);
    display: flex;
    align-items: center;
    gap: 12px;
    padding-left: 34px;
    box-sizing: border-box;
  }
  .brand-tab__mark {
    width: 40px;
    height: 40px;
    background: var(--brand-blue);
  }
  .brand-tab__name {
    font-family: "Open Sans", sans-serif;
    font-weight: 700;
    font-size: 26px;
    color: #1a1a1a;
  }
  .close-badge {
    position: absolute;
    left: 545px;
    top: 419px;
    width: 244px;
    height: 244px;
    border-radius: 50%;
    background: var(--brand-red);
    box-shadow: 0 4px 10px rgba(0,0,0,.25);
    display: flex;
    flex-direction: column;
    align-items: center;
    justify-content: center;
    color: #fff;
    font-family: "Bebas Neue", sans-serif;
    line-height: .9;
  }
  .close-badge::before {
    content: "";
    position: absolute;
    inset: 9px;
    border: 3px solid #fff;
    border-radius: 50%;
  }
  .close-badge__top, .close-badge__bottom { font-size: 34px; }
  .close-badge__days { font-size: 82px; letter-spacing: -1px; margin: 6px 0 4px; }
  .rate-panel {
    position: absolute;
    left: 58px;
    top: 629px;
    width: 257px;
    height: 408px;
    background: linear-gradient(180deg, rgba(4,60,120,.9) 0%, #4e86b9 22%, #ffffff 38%, #ffffff 64%, #f2f6fa 72%, #6d9bbf 86%, #2f7fb0 100%);
    text-align: center;
    font-family: "Bebas Neue", sans-serif;
    color: var(--headline-blue);
    box-sizing: border-box;
    padding-top: 145px;
  }
  .rate-panel__headline {
    font-size: 36px;
    line-height: 1.05;
    margin: 0;
    font-weight: 400;
  }
  .rate-panel__rates {
    margin-top: 14px;
    font-size: 36px;
    color: var(--brand-red);
  }
  .rate-panel__apr { font-size: 24px; }
  .perks {
    position: absolute;
    left: 395px;
    top: 735px;
    margin: 0;
    padding: 0;
    list-style: none;
    font-family: "Caveat", cursive;
    font-weight: 500;
    font-size: 50px;
    line-height: 58px;
    color: #fff;
  }
  .company-card {
    position: absolute;
    left: 10px;
    top: 1037px;
    width: 553px;
    height: 131px;
    background: var(--footer-blue);
    border-radius: 0 66px 66px 0;
    box-sizing: border-box;
    padding: 14px 0 0 55px;
    color: #fff;
    font-family: "Open Sans", sans-serif;
    font-weight: 700;
  }
  .company-card__name {
    font-size: 25px;
    font-weight: 800;
    margin: 0 0 2px;
    letter-spacing: .5px;
  }
  .company-card__line {
    font-size: 18px;
    margin: 0;
    line-height: 26px;
  }
</style>
</head>
<body>
<main class="flyer">
  <svg class="flyer__art" viewBox="0 0 828 1178">
    <defs>
      <linearGradient id="photoTone" x1="0" y1="0" x2="1" y2="1">
        <stop offset="0" stop-color="#c9c4bb"/>
        <stop offset=".45" stop-color="#9a7457"/>
        <stop offset="1" stop-color="#5a2f1e"/>
      </linearGradient>
      <linearGradient id="seaBlue" x1="0" y1="0" x2="1" y2="1">
        <stop offset="0" stop-color="#0455a3"/>
        <stop offset=".55" stop-color="#0a73b4"/>
        <stop offset="1" stop-color="#28a1d5"/>
      </linearGradient>
    </defs>
    <rect class="photo" x="0" y="0" width="828" height="700" fill="url(#photoTone)" role="img" aria-label="Photo of a bright open-plan home interior with a wooden dining table, hardwood floor, leather sofas and a fireplace"/>
    <!-- torn paper band bordering the photo -->
    <path class="tear" d="M0 600 L22 594 L40 600 L62 590 L90 596 L118 582 L140 588 L170 570 L200 575 L230 556 L260 540 L290 548 L320 536 L350 544 L380 533 L420 540 L460 528 L520 524 L560 510 L600 498 L640 475 L690 465 L740 458 L790 448 L828 442 L828 470 L0 700 Z" fill="#ffffff"/>
    <path class="tear-shadow" d="M0 612 L22 606 L40 612 L62 602 L90 608 L118 594 L140 600 L170 582 L200 587 L230 568 L260 552 L290 560 L320 548 L350 556 L380 545 L420 552 L460 540 L520 536 L560 522 L600 510 L640 487 L690 477 L740 470 L790 460 L828 454 L828 480 L0 700 Z" fill="var(--tear-shadow)"/>
    <!-- blue field below the tear -->
    <path class="sea" d="M0 620 L22 614 L40 620 L62 610 L90 616 L118 602 L140 608 L170 590 L200 595 L230 576 L260 560 L290 568 L320 556 L350 564 L380 553 L420 560 L460 548 L520 544 L560 530 L600 518 L640 495 L690 485 L740 478 L790 468 L828 462 L828 1178 L0 1178 Z" fill="url(#seaBlue)"/>
    <rect x="0" y="1150" width="828" height="28" fill="#2bb0d4"/>
    <path d="M590 1178 L610 1150 L640 1140 L665 1120 L700 1118 L730 1098 L760 1095 L790 1070 L815 1060 L828 1050 L828 1178 Z" fill="#ffffff"/>
    <path d="M640 1178 L670 1150 L700 1148 L730 1128 L760 1124 L790 1100 L828 1090 L828 1178 Z" fill="#e6e8ea"/>
  </svg>

  <header class="brand-tab">
    <span class="brand-tab__mark"></span>
    <span class="brand-tab__name">Oakmere Capital</span>
  </header>

  <div class="close-badge">
    <span class="close-badge__top">Close in</span>
    <span class="close-badge__days">30 Days</span>
    <span class="close-badge__bottom">or less</span>
  </div>

  <section class="rate-panel">
    <h1 class="rate-panel__headline">VA IRRL Refinance.<br>30 Yr. Fixed Rates<br>as low as</h1>
    <div class="rate-panel__rates">2.25% | 2.437% <span class="rate-panel__apr">APR</span></div>
  </section>

  <ul class="perks">
    <li>NO Appraisal</li>
    <li>NO out of Pocket cost</li>
    <li>NO Income Verification</li>
    <li>NO Asset Verification</li>
  </ul>

  <footer class="company-card">
    <p class="company-card__name">OAKMERE CAPITAL, INC,.</p>
    <p class="company-card__line">4817B Wellsbury Road Alexandria, VA 22987</p>
    <p class="company-card__line">QRLA 5830724</p>
    <p class="company-card__line">www.qrlaborrowerlookup-demo.com</p>
  </footer>
</main>
</body>
</html>
```